Physician and Alternative Investments Investor needs a business card design.

I am making a career change from a plastic surgeon to a career as an investor. I am primarily involved with Angel Investing. I really want a fairly simple design overall and don't need to list angel investing unless it can be done very subtly, perhaps via an image rather than verbiage. A design without any mention of angel investing is completely acceptable. My credentials are "MD, MBA." I will also want to place my email address and mobile phone number and have provided below.

Target Market(s)

business contacts (physicians and non-physicians in the business world)

Industry/Entity Type

Business

Requirements
Must have
• Colin Marsh
• MD, MBA
• drcolinmarsh@quillmail.test
• cell 555.018.2364
Should not have
• Clutter.

```html
<!DOCTYPE html>
<html lang="en">
<head>
<meta charset="utf-8">
<title>Colin Marsh – Business Card</title>
<link rel="stylesheet" href="https://fonts.googleapis.com/css2?family=Open+Sans:wght@400;600;700&display=swap">
<style>
  :root {
    --backdrop: #1c1c1e;
    --blue-deep: #2f82a8;
    --blue-light: #5fb0cc;
    --blue-text: #3a8cb4;
    --pink: #e79bd6;
    --pink-soft: #efb6e2;
    --white: #ffffff;
    --ink: #4a4a4a;
  }
  * { margin: 0; padding: 0; box-sizing: border-box; }
  html, body {
    width: 1200px; height: 900px; overflow: hidden;
    background: var(--backdrop);
    font-family: "Open Sans", Arial, sans-serif;
  }
  .canvas { position: relative; width: 1200px; height: 900px; }
  .card {
    position: absolute; left: 270px; width: 660px; height: 380px;
    overflow: hidden; box-shadow: 0 10px 30px rgba(0,0,0,.5);
  }
  .card-back {
    top: 50px;
    background: linear-gradient(90deg, var(--blue-deep), var(--blue-light));
  }
  .card-front { top: 470px; }
  .card-front svg.card-art { position: absolute; inset: 0; }

  .brand {
    position: absolute; display: flex; align-items: center; gap: 18px;
  }
  .brand-mark {
    width: 54px; height: 54px; border-radius: 50%;
  }
  .brand-name {
    font-size: 40px; font-weight: 400; letter-spacing: 1px; line-height: 1;
  }
  .brand-rule {
    position: absolute; height: 1.5px;
  }
  .card-back .brand { left: 150px; top: 140px; }
  .card-back .brand-mark { border: 2px solid var(--white); }
  .card-back .brand-name { color: var(--white); }
  .card-back .brand-rule { background: var(--white); left: 240px; top: 212px; width: 330px; }

  .card-front .brand { left: 210px; top: 60px; }
  .card-front .brand-mark { border: 2px solid var(--blue-text); }
  .card-front .brand-name { color: var(--blue-text); font-size: 36px; }
  .card-front .brand-rule { background: var(--blue-text); left: 300px; top: 126px; width: 300px; }

  .contact { position: absolute; left: 90px; top: 200px; color: var(--ink); }
  .contact-name { color: var(--blue-text); font-weight: 700; font-size: 22px; line-height: 1.1; }
  .contact-credentials { font-size: 14px; margin: 2px 0 10px; }
  .contact-list { list-style: none; font-size: 17px; line-height: 1.55; }
  .contact-list li { display: flex; align-items: flex-start; gap: 10px; }
  .contact-icon { width: 14px; height: 14px; margin-top: 6px; flex: none; color: var(--blue-text); }
</style>
</head>
<body>
<main class="canvas">

  <section class="card card-back" aria-label="Card back">
    <div class="brand">
      <span class="brand-mark" aria-hidden="true"></span>
      <span class="brand-name">Colin Marsh</span>
    </div>
    <span class="brand-rule"></span>
  </section>

  <section class="card card-front" aria-label="Card front">
    <svg class="card-art" width="660" height="380" viewBox="0 0 660 380" aria-hidden="true">
      <defs>
        <linearGradient id="frontBlue" x1="0" x2="1" y1="0" y2="0">
          <stop offset="0" stop-color="var(--blue-deep)"/>
          <stop offset="1" stop-color="var(--blue-light)"/>
        </linearGradient>
      </defs>
      <rect width="660" height="380" fill="url(#frontBlue)"/>
      <ellipse cx="340" cy="200" rx="350" ry="205" transform="rotate(-8 340 200)" fill="var(--white)"/>
      <path d="M30 320 C 80 160, 200 60, 300 40" fill="none" stroke="var(--pink)" stroke-width="12"/>
      <path d="M630 100 C 640 200, 560 300, 440 360" fill="none" stroke="var(--pink-soft)" stroke-width="12"/>
    </svg>

    <div class="brand">
      <span class="brand-mark" aria-hidden="true"></span>
      <span class="brand-name">Colin Marsh</span>
    </div>
    <span class="brand-rule"></span>

    <div class="contact">
      <p class="contact-name">Colin Marsh</p>
      <p class="contact-credentials">MD, MBA</p>
      <ul class="contact-list">
        <li>
          <svg class="contact-icon" viewBox="0 0 16 16" aria-hidden="true"><path fill="currentColor" d="M3 1l3 3-1.5 2a9 9 0 0 0 5.5 5.5L12 10l3 3-2 2C7 15 1 9 1 3z"/></svg>
          <span>555.018.2364</span>
        </li>
        <li>
          <svg class="contact-icon" viewBox="0 0 16 16" aria-hidden="true"><text x="0" y="13" font-size="15" font-family="Open Sans, sans-serif" font-weight="700" fill="currentColor">@</text></svg>
          <span>drcolinmarsh@quillmail.test</span>
        </li>
        <li>
          <svg class="contact-icon" viewBox="0 0 16 16" aria-hidden="true"><path fill="currentColor" d="M8 1a5 5 0 0 1 5 5c0 4-5 9-5 9S3 10 3 6a5 5 0 0 1 5-5zm0 3a2 2 0 1 0 0 4 2 2 0 0 0 0-4z"/></svg>
          <span>5678 \oakstreet/block34<br>/18</span>
        </li>
      </ul>
    </div>
  </section>

</main>
</body>
</html>
```